I need creative and unique business card design using my company logo. Ok to change logo color. We are a small brokerage doing both Real Estate and Mortgage services. Need to have the follow on business card;
1. agent name - Mila Fenton - Realtor
2. cell - 949-555-0182
3. license number - DRE 04917362
4. business name - Brightway Estates & Lending, Inc
5. business office - 626-555-0147
6. business address - 287 W. Larkmoor Ave #214, Arcadia CA 91088
7. business logo - attached (ok to use different color on logo)

```html
<!DOCTYPE html>
<html lang="en">
<head>
<meta charset="utf-8">
<title>Mila Fenton – Business Card</title>
<link href="https://fonts.googleapis.com/css2?family=Open+Sans:wght@400;600;700&display=swap" rel="stylesheet">
<style>
  :root{
    --stage:#222222;
    --paper:#ffffff;
    --ink:#111111;
    --brand-blue:#1f5fc4;
    --accent-blue:#0a78d6;
    --band-light:#1c8fe6;
    --band-dark:#0b5fb8;
    --navy:#28359a;
    --navy-deep:#1f2a80;
    --navy-light:#3346b0;
    --mist:#e2e3f2;
    --mist-soft:#eef2fb;
  }
  *{box-sizing:border-box;margin:0;padding:0}
  html,body{width:1200px;height:780px;overflow:hidden;background:var(--stage)}
  body{font-family:"Open Sans",Arial,sans-serif;position:relative}

  .card{position:absolute;top:240px;width:520px;height:300px;overflow:hidden;box-shadow:0 14px 30px rgba(0,0,0,.45)}
  .card--front{left:40px;background:var(--paper)}
  .card--back{left:640px;background:var(--navy)}

  /* front */
  .brand{position:absolute;left:30px;top:30px;display:flex;align-items:center;gap:10px}
  .brand__square{width:34px;height:34px;background:var(--brand-blue)}
  .brand__name{font-weight:600;font-size:13px;letter-spacing:.06em;color:var(--brand-blue);line-height:1.25;width:150px}

  .address{position:absolute;left:30px;top:118px;font-size:12px;line-height:1.45;color:var(--ink)}
  .phones{position:absolute;left:30px;top:166px;font-size:12px;line-height:1.6;color:var(--ink);list-style:none}
  .phones li{display:flex;align-items:center;gap:7px}
  .phones svg{width:11px;height:11px;flex:none}

  .backdrop-area{position:absolute;left:268px;top:62px;width:252px;height:238px;
    background:linear-gradient(160deg,var(--mist) 0%,var(--mist-soft) 100%)}

  .agent{position:absolute;left:330px;top:116px}
  .agent__name{font-weight:700;font-size:25px;color:var(--accent-blue);line-height:1.1}
  .agent__role{font-weight:600;font-size:13px;color:var(--ink);margin-top:3px;margin-left:60px}

  .accent-band{position:absolute;right:0;top:176px;width:52px;height:44px;
    background:linear-gradient(180deg,var(--band-light),var(--band-dark))}

  .license{position:absolute;left:318px;top:262px;font-size:13px;color:var(--ink)}
  .license__label{color:var(--accent-blue);font-weight:600;margin-right:4px}

  /* back */
  .pattern{position:absolute;inset:0;
    background:
      radial-gradient(circle at 30% 25%, var(--navy-light) 0, transparent 55%),
      linear-gradient(135deg,var(--navy) 0%,var(--navy-deep) 100%)}
  .back-brand{position:absolute;left:300px;top:168px;display:flex;align-items:center;gap:6px}
  .back-brand__square{width:14px;height:14px;background:var(--paper)}
  .back-brand__name{font-weight:600;font-size:7px;letter-spacing:.08em;color:var(--paper);width:80px;line-height:1.3}
</style>
</head>
<body>

<section class="card card--front" aria-label="Business card front">
  <div class="backdrop-area" role="img" aria-label="Soft pale decorative backdrop area"></div>

  <div class="brand">
    <span class="brand__square"></span>
    <span class="brand__name">Brightway Estates &amp; Lending, Inc</span>
  </div>

  <p class="address">287 W. Larkmoor Ave #214,<br>Arcadia CA 91088</p>

  <ul class="phones">
    <li>
      <svg viewBox="0 0 12 12" aria-hidden="true"><rect x="3" y="0.8" width="6" height="10.4" rx="1" fill="none" stroke="#0a78d6" stroke-width="1.2"/></svg>
      949-555-0182
    </li>
    <li>
      <svg viewBox="0 0 12 12" aria-hidden="true"><path d="M2.5 1.5c1-.6 2 1.6 2 2.2 0 .7-1 .9-.8 1.6.4 1.2 1.5 2.3 2.7 2.7.7.2.9-.8 1.6-.8.6 0 2.8 1 2.2 2-.6 1-1.6 1.6-2.9 1.2C4.6 9.6 2.4 7.4 1.6 4.6 1.2 3.2 1.6 2.1 2.5 1.5z" fill="#0a78d6"/></svg>
      626-555-0147
    </li>
  </ul>

  <div class="agent">
    <h1 class="agent__name">Mila Fenton</h1>
    <p class="agent__role">Realtor</p>
  </div>

  <div class="accent-band"></div>

  <p class="license"><span class="license__label">DRE</span>04917362</p>
</section>

<section class="card card--back" aria-label="Business card back">
  <div class="pattern" role="img" aria-label="Repeating embossed decorative pattern on navy"></div>
  <div class="back-brand">
    <span class="back-brand__square"></span>
    <span class="back-brand__name">Brightway Estates &amp; Lending, Inc</span>
  </div>
</section>

</body>
</html>
```